Zo Fen smart screen Flyer design

Hi,

Please see attached file as I have done up a very very basic flyer just with the information that will need to be presented.

Please don't go with this as a format I would like, as I have no design skills at all.

I'm looking for something that is basic but professional looking capturing this information.
I would prefer if the symbols were changed so they were all consistent and the colour scheme worked together with the logo.

If you can use the picture of the screen provided as I will replace this once my product has its photoshoot.

Thanks!

```html
<!DOCTYPE html>
<html lang="en">
<head>
<meta charset="utf-8">
<title>Zo Fen Smart Screen Flyer</title>
<link rel="stylesheet" href="https://fonts.googleapis.com/css2?family=Ubuntu:wght@400;500;700&display=swap">
<style>
  :root {
    --paper: #ffffff;
    --ink: #1a1a1a;
    --panel-yellow: #fcdc00;
    --grass: #6f9a3c;
    --grass-light: #a9c46a;
    --sky-red: #d8434f;
  }
  * { margin: 0; padding: 0; box-sizing: border-box; }
  html, body { width: 849px; height: 1200px; overflow: hidden; background: var(--paper); }
  .flyer {
    position: relative; width: 849px; height: 1200px; overflow: hidden;
    background: var(--paper); color: var(--ink);
    font-family: "Ubuntu", sans-serif;
  }
  .brand { position: absolute; left: 49px; top: 58px; width: 252px; }
  .brand-name {
    font-size: 54px; font-weight: 700; line-height: 1; letter-spacing: 2px;
    color: var(--ink);
  }
  .brand-tagline {
    margin-top: 12px; font-size: 11px; font-weight: 500; letter-spacing: 10.5px;
    color: var(--ink);
  }
  .product-shot {
    position: absolute; left: 49px; top: 192px; width: 375px; height: 598px;
    background: linear-gradient(180deg, var(--sky-red) 0%, #c9b07a 18%, var(--grass) 45%, var(--grass-light) 70%, #ffffff 100%);
  }
  .benefits {
    position: absolute; left: 49px; top: 853px; width: 375px; list-style: none;
  }
  .benefits li {
    position: relative; padding-left: 26px; margin-bottom: 24px;
    font-size: 16.5px; line-height: 22px; text-align: justify;
  }
  .benefits .tick { position: absolute; left: 0; top: 3px; width: 14px; height: 14px; }
  .features-panel {
    position: absolute; left: 455px; top: 0; width: 359px; height: 1200px;
    background: var(--panel-yellow); text-align: center;
  }
  .feature { position: absolute; left: 0; width: 359px; }
  .feature svg { display: block; margin: 0 auto; }
  .feature-title { font-size: 14.5px; font-weight: 500; line-height: 19px; }
  .feature-text { font-size: 13.6px; line-height: 19px; padding: 0 22px; }
  .contact-rule {
    position: absolute; left: 21px; top: 1046px; width: 314px; height: 0;
    border-top: 1.5px solid var(--ink);
  }
  .contact { position: absolute; left: 0; top: 1100px; width: 359px; }
  .contact-phone { font-size: 16.5px; line-height: 22px; }
  .contact-phone strong { font-weight: 500; font-size: 18px; }
  .contact-web { font-size: 14.5px; line-height: 20px; }
</style>
</head>
<body>
<main class="flyer">
  <header class="brand">
    <div class="brand-name">ZO FEN</div>
    <div class="brand-tagline">SMART SCREEN</div>
  </header>

  <div class="product-shot" role="img" aria-label="Product photo of an outdoor LED screen showing a child playing with a ball on grass"></div>

  <ul class="benefits">
    <li><svg class="tick" viewBox="0 0 14 14"><rect x="1" y="2" width="11" height="11" fill="none" stroke="#1a1a1a" stroke-width="1.6"/><path d="M3.5 7.5l2.5 2.5 7-8" fill="none" stroke="#1a1a1a" stroke-width="1.8"/></svg>Bring attnetion to your bussiness with your own hd led display.</li>
    <li><svg class="tick" viewBox="0 0 14 14"><rect x="1" y="2" width="11" height="11" fill="none" stroke="#1a1a1a" stroke-width="1.6"/><path d="M3.5 7.5l2.5 2.5 7-8" fill="none" stroke="#1a1a1a" stroke-width="1.8"/></svg>our displays can be mounted outdoors on walls, roofs, xed signs, trailer mounted ect.</li>
    <li><svg class="tick" viewBox="0 0 14 14"><rect x="1" y="2" width="11" height="11" fill="none" stroke="#1a1a1a" stroke-width="1.6"/><path d="M3.5 7.5l2.5 2.5 7-8" fill="none" stroke="#1a1a1a" stroke-width="1.8"/></svg>we also do indoor led screens for shop fronts and display stands.</li>
    <li><svg class="tick" viewBox="0 0 14 14"><rect x="1" y="2" width="11" height="11" fill="none" stroke="#1a1a1a" stroke-width="1.6"/><path d="M3.5 7.5l2.5 2.5 7-8" fill="none" stroke="#1a1a1a" stroke-width="1.8"/></svg>All screens are custom built to your requirements including size, shape and even curved display</li>
  </ul>

  <aside class="features-panel">
    <section class="feature" style="top:120px">
      <svg width="50" height="58" viewBox="0 0 50 58">
        <text x="2" y="52" font-family="Ubuntu, sans-serif" font-weight="700" font-size="32" fill="#1a1a1a">4G</text>
        <path d="M34 20a6 6 0 0 1 6 6M34 12a14 14 0 0 1 14 14M34 4a22 22 0 0 1 22 22" fill="none" stroke="#1a1a1a" stroke-width="3" transform="translate(-8,0)"/>
      </svg>
      <div class="feature-title" style="margin-top:26px">4G CAPABLE</div>
      <p class="feature-text">Change screen content with a click of the mouse anywhere in the world</p>
    </section>

    <section class="feature" style="top:288px">
      <svg width="48" height="40" viewBox="0 0 48 40">
        <path d="M3 13a30 30 0 0 1 42 0" fill="none" stroke="#1a1a1a" stroke-width="5" stroke-linecap="round"/>
        <path d="M11 21a19 19 0 0 1 26 0" fill="none" stroke="#1a1a1a" stroke-width="5" stroke-linecap="round"/>
        <circle cx="24" cy="33" r="6" fill="#1a1a1a"/>
      </svg>
      <div class="feature-title" style="margin-top:29px">WIFI CAPABLE</div>
      <p class="feature-text">Change screen content with a PC, tablet or mobile phone an easy to use app</p>
    </section>

    <section class="feature" style="top:450px">
      <svg width="48" height="48" viewBox="0 0 48 48" stroke="#1a1a1a" stroke-width="3.5" stroke-linecap="round" fill="none">
        <circle cx="24" cy="24" r="8"/>
        <path d="M24 2v7M24 39v7M2 24h7M39 24h7M8.5 8.5l5 5M34.5 34.5l5 5M8.5 39.5l5-5M34.5 13.5l5-5"/>
      </svg>
      <div class="feature-title" style="margin-top:30px">INTELIGENT BRIGHTNESS CONTROL</div>
      <p class="feature-text">Screen will automatically adjust to suit ambiant light improving screen viewing quality and saving in power consumption</p>
    </section>

    <section class="feature" style="top:636px">
      <svg width="48" height="48" viewBox="0 0 48 48" fill="none" stroke="#1a1a1a" stroke-width="2.5">
        <path d="M8 20v18h32V20H32"/>
        <path d="M2 44l4-6h36l4 6z" fill="#1a1a1a"/>
        <rect x="27" y="2" width="6" height="26" rx="3"/>
        <circle cx="30" cy="30" r="4.5" fill="#1a1a1a"/>
        <path d="M15 6v12M9 12h12M11 8l8 8M19 8l-8 8" stroke-width="1.8"/>
      </svg>
      <div class="feature-title" style="margin-top:48px">ONLINE MONITORING</div>
      <p class="feature-text">Monitor cabinet temperature and humidity plus more in real time online. Recieve alerts via email</p>
    </section>

    <section class="feature" style="top:822px">
      <svg width="36" height="56" viewBox="0 0 36 56">
        <path d="M11 30h14v22l-7-4-7 4z" fill="#1a1a1a"/>
        <circle cx="18" cy="18" r="14" fill="#1a1a1a"/>
        <path d="M18 2l4 4h5v5l4 4-4 4v5h-5l-4 4-4-4H9v-5l-4-4 4-4V6h5z" fill="#1a1a1a"/>
        <path d="M18 10l2.3 5 5.2.5-4 3.5 1.2 5.2-4.7-2.8-4.7 2.8 1.2-5.2-4-3.5 5.2-.5z" fill="#fcdc00"/>
      </svg>
      <div class="feature-title" style="margin-top:22px">HIGH QUALITY PRODUCTS</div>
      <p class="feature-text">Setting high standard for colour, brightness and sharpness these LED modules will create attention</p>
    </section>

    <div class="contact-rule"></div>

    <section class="contact">
      <p class="contact-phone"><strong>1300 ZOFENWA</strong> for a free quote</p>
      <p class="contact-web">info@zofenwa.com.au | www.zofenwa.com.au</p>
    </section>
  </aside>
</main>
</body>
</html>
```